Accounting business needs business card

I have a business card but need something better. I want the colour changed and the design to be better. I have uploaded a picture of my new sign that is grey in colour, i would like to incorporate these colours.

```html
<!DOCTYPE html>
<html lang="en">
<head>
<meta charset="utf-8">
<title>Keystone Tax – Business Card</title>
<link rel="stylesheet" href="https://fonts.googleapis.com/css2?family=Montserrat:wght@400;500;600;700&display=swap">
<style>
  :root {
    --backdrop: #3b3b3d;
    --metal-light: #d2d2d6;
    --metal-mid: #bdbdc2;
    --metal-dark: #aeaeb4;
    --ink: #151515;
    --badge-dark: #5a5a60;
    --badge-mid: #808087;
    --badge-soft: #9a9aa1;
  }
  * { box-sizing: border-box; margin: 0; padding: 0; }
  html, body {
    width: 871px; height: 1200px; overflow: hidden;
    background: var(--backdrop);
    font-family: "Montserrat", sans-serif;
    color: var(--ink);
  }
  .canvas { position: relative; width: 871px; height: 1200px; }

  .card {
    position: absolute; left: 55px; width: 760px; height: 434px;
    border-radius: 26px; overflow: hidden;
    background:
      repeating-linear-gradient(0deg, rgba(255,255,255,.10) 0 1px, rgba(0,0,0,.05) 1px 2px, transparent 2px 4px),
      linear-gradient(100deg, var(--metal-mid) 0%, var(--metal-light) 45%, var(--metal-dark) 100%);
    box-shadow: 0 18px 40px rgba(0,0,0,.45);
  }
  .card--front { top: 120px; }
  .card--back { top: 646px; }

  /* front */
  .brand-circle {
    position: absolute; left: 52px; top: 62px;
    width: 120px; height: 120px; border: 3px solid var(--ink); border-radius: 50%;
  }
  .wordmark {
    position: absolute; left: 205px; top: 98px;
    font-size: 40px; font-weight: 500; letter-spacing: 15px;
  }
  .person {
    position: absolute; right: 48px; top: 178px; text-align: right; line-height: 1.25;
  }
  .person__name { font-size: 30px; font-weight: 700; letter-spacing: 3px; }
  .person__creds, .person__role { font-size: 17px; font-weight: 500; }
  .divider {
    position: absolute; left: 60px; top: 268px; width: 330px; height: 2px;
    background: linear-gradient(90deg, transparent, var(--ink) 40%);
  }
  .contact { position: absolute; left: 56px; top: 296px; list-style: none; }
  .contact__item { display: flex; align-items: center; gap: 10px; font-weight: 500; }
  .contact__item--phone { font-size: 28px; }
  .contact__item--mail, .contact__item--web { font-size: 19px; margin-top: 4px; }
  .contact__icon { width: 18px; height: 18px; flex: none; }

  .partners { position: absolute; right: 48px; top: 290px; display: flex; align-items: center; gap: 22px; }
  .badge { flex: none; }
  .badge--round { width: 72px; height: 72px; border-radius: 50%; background: var(--badge-mid); }
  .badge--seal { width: 72px; height: 72px; border-radius: 50%; border: 3px solid var(--badge-dark); }
  .member { display: flex; flex-direction: column; align-items: flex-start; gap: 5px; }
  .member__note { font-size: 9px; font-weight: 600; }
  .badge--rect { width: 150px; height: 64px; background: var(--badge-soft); }

  /* back */
  .back-mark {
    position: absolute; left: 50%; top: 78px; transform: translateX(-50%);
    width: 160px; height: 160px; border: 3px solid var(--ink); border-radius: 50%;
    display: grid; place-items: center;
    font-size: 20px; font-weight: 600; letter-spacing: 3px;
  }
  .back-web {
    position: absolute; left: 0; right: 0; top: 300px; text-align: center;
    font-size: 26px; font-weight: 500; letter-spacing: 6px;
  }
</style>
</head>
<body>
<main class="canvas">
  <section class="card card--front" aria-label="Card front">
    <div class="brand-circle"></div>
    <h1 class="wordmark">KEYSTONE TAX</h1>
    <div class="person">
      <p class="person__name">TOM HARLAND</p>
      <p class="person__creds">CPA, MTAX, BCOM (Acc &amp; Fin)</p>
      <p class="person__role">Taxation and Business Accountant</p>
    </div>
    <div class="divider"></div>
    <ul class="contact">
      <li class="contact__item contact__item--phone">
        <svg class="contact__icon" viewBox="0 0 24 24"><path fill="currentColor" d="M6.6 10.8a15 15 0 0 0 6.6 6.6l2.2-2.2a1 1 0 0 1 1-.25 11.4 11.4 0 0 0 3.6.57 1 1 0 0 1 1 1V20a1 1 0 0 1-1 1A17 17 0 0 1 3 4a1 1 0 0 1 1-1h3.5a1 1 0 0 1 1 1c0 1.25.2 2.45.57 3.57a1 1 0 0 1-.25 1z"/></svg>
        0412 555 019
      </li>
      <li class="contact__item contact__item--mail">
        <svg class="contact__icon" viewBox="0 0 24 24"><path fill="currentColor" d="M3 5h18v14H3zm2 2v.5l7 4.5 7-4.5V7z"/></svg>
        tom@keystonetax.com.au
      </li>
      <li class="contact__item contact__item--web">
        <svg class="contact__icon" viewBox="0 0 24 24"><circle cx="12" cy="12" r="9" fill="none" stroke="currentColor" stroke-width="2"/><path d="M3 12h18M12 3c3 3 3 15 0 18M12 3c-3 3-3 15 0 18" fill="none" stroke="currentColor" stroke-width="1.6"/></svg>
        www.keystonetax.com.au
      </li>
    </ul>
    <div class="partners">
      <div class="badge badge--round"></div>
      <div class="badge badge--seal"></div>
      <div class="member">
        <p class="member__note">Keystone Tax is a member firm</p>
        <div class="badge badge--rect"></div>
      </div>
    </div>
  </section>

  <section class="card card--back" aria-label="Card back">
    <div class="back-mark">KEYSTONE</div>
    <p class="back-web">WWW.KEYSTONETAX.COM.AU</p>
  </section>
</main>
</body>
</html>
```